Garnett and Lyle Personal Injury Billboard

We'd like a clean/modern billboard to build brand awareness for our law firm in the area of personal injury. Ideally, we like the word "Injured?" or something similar in large lettering.

I'm attaching images, logo and award badges which could be used. The billboards will be 14x48 ft and 10.6x36.

We are open to different color ideas, fonts, and artwork. Creative but not too busy with wording. Our web page is www.kgarnettfirm.example

Garnett & Lyle Law Firm
(555) 318-4092

```html
<!DOCTYPE html>
<html lang="en">
<head>
<meta charset="utf-8">
<title>Garnett and Lyle Personal Injury Billboard</title>
<link rel="stylesheet" href="https://fonts.googleapis.com/css2?family=Montserrat:wght@600;700;800;900&display=swap">
<style>
  :root {
    --canvas: #cbcbcb;
    --blue: #0a63b3;
    --blue-deep: #0b3d73;
    --black: #0d0d10;
    --red: #dc1f26;
    --red-deep: #b8131a;
    --white: #ffffff;
    --photo-light: #9ea3a8;
    --photo-dark: #5c6167;
    --badge: #1e8fd6;
  }
  html, body {
    margin: 0;
    padding: 0;
    width: 1059px;
    height: 1200px;
    overflow: hidden;
    background: var(--canvas);
  }
  .billboard {
    position: absolute;
    left: 30px;
    top: 455px;
    width: 1000px;
    height: 291px;
    overflow: hidden;
    font-family: "Montserrat", Arial, sans-serif;
    color: var(--white);
  }
  .billboard__bg { position: absolute; inset: 0; }
  .headline {
    position: absolute;
    left: 30px;
    top: 2px;
    margin: 0;
    font-size: 134px;
    font-weight: 900;
    letter-spacing: -3px;
    line-height: 1;
    text-shadow: 5px 4px 0 var(--black);
  }
  .tagline {
    position: absolute;
    left: 34px;
    top: 130px;
    margin: 0;
    font-size: 35px;
    font-weight: 800;
    letter-spacing: 0.5px;
    line-height: 1;
  }
  .tagline__accent { color: var(--red); }
  .award-badge {
    position: absolute;
    left: 25px;
    top: 186px;
    width: 66px;
    height: 89px;
    background: var(--badge);
    border: 2px solid var(--white);
    box-sizing: border-box;
  }
  .phone {
    position: absolute;
    left: 118px;
    top: 180px;
    margin: 0;
    font-size: 77px;
    font-weight: 800;
    line-height: 1;
    letter-spacing: -0.5px;
    white-space: nowrap;
  }
  .website {
    position: absolute;
    left: 125px;
    top: 258px;
    width: 355px;
    font-size: 21px;
    font-weight: 700;
    line-height: 1;
    white-space: nowrap;
  }
  .consult {
    position: absolute;
    left: 491px;
    top: 256px;
    width: 194px;
    height: 28px;
    background: var(--black);
    font-size: 16px;
    font-weight: 700;
    line-height: 28px;
    text-align: center;
    white-space: nowrap;
  }
  .firm-name {
    position: absolute;
    left: 770px;
    top: 22px;
    width: 220px;
    display: flex;
    align-items: center;
    gap: 12px;
    font-size: 26px;
    font-weight: 700;
    line-height: 1.15;
  }
  .firm-name__mark {
    flex: none;
    width: 14px;
    height: 14px;
    background: var(--white);
  }
  .firm-name__line { display: block; white-space: nowrap; }
  .attorney-photo {
    position: absolute;
    top: 122px;
    height: 139px;
  }
  .attorney-photo--first { left: 738px; width: 165px; }
  .attorney-photo--second { left: 903px; width: 97px; }
  .attorney-names {
    position: absolute;
    left: 689px;
    top: 261px;
    width: 311px;
    height: 30px;
  }
  .attorney-name {
    position: absolute;
    top: 8px;
    font-size: 14px;
    font-weight: 700;
    line-height: 1;
    white-space: nowrap;
  }
  .attorney-name--first { left: 43px; }
  .attorney-name--second { left: 209px; }
</style>
</head>
<body>
  <div class="billboard">
    <svg class="billboard__bg" width="1000" height="291" viewBox="0 0 1000 291" aria-hidden="true">
      <defs>
        <linearGradient id="topBand" x1="0" y1="0" x2="1" y2="0">
          <stop offset="0" stop-color="var(--blue)"/>
          <stop offset="0.35" stop-color="var(--blue-deep)"/>
          <stop offset="0.7" stop-color="var(--black)"/>
          <stop offset="1" stop-color="var(--black)"/>
        </linearGradient>
      </defs>
      <rect width="1000" height="172" fill="url(#topBand)"/>
      <rect y="172" width="1000" height="119" fill="var(--red)"/>
      <polygon points="823,172 1000,172 1000,291 750,291" fill="var(--red-deep)"/>
      <polygon points="705,261 1000,261 1000,291 689,291" fill="var(--blue)"/>
    </svg>

    <h1 class="headline">INJURED?</h1>
    <p class="tagline"><span class="tagline__accent">NO FEES,</span> UNLESS WE WIN</p>

    <div class="award-badge" role="img" aria-label="Community award badge"></div>

    <p class="phone">(555) 318-4092</p>
    <div class="website">www.kgarnettfirm.example</div>
    <div class="consult">FREE CONSULTATION</div>

    <div class="firm-name">
      <span class="firm-name__mark"></span>
      <span><span class="firm-name__line">Garnett &amp; Lyle</span><span class="firm-name__line">Law Firm</span></span>
    </div>

    <svg class="attorney-photo attorney-photo--first" viewBox="0 0 165 139" preserveAspectRatio="none" role="img" aria-label="Portrait photo of attorney Keith A. Garnett">
      <defs>
        <linearGradient id="photoA" x1="0" y1="0" x2="0" y2="1">
          <stop offset="0" stop-color="var(--photo-light)" stop-opacity="0.25"/>
          <stop offset="1" stop-color="var(--photo-dark)"/>
        </linearGradient>
      </defs>
      <rect width="165" height="139" fill="url(#photoA)"/>
    </svg>
    <svg class="attorney-photo attorney-photo--second" viewBox="0 0 97 139" preserveAspectRatio="none" role="img" aria-label="Portrait photo of attorney Owen Lyle">
      <defs>
        <linearGradient id="photoB" x1="0" y1="0" x2="0" y2="1">
          <stop offset="0" stop-color="var(--photo-light)" stop-opacity="0.25"/>
          <stop offset="1" stop-color="var(--photo-dark)"/>
        </linearGradient>
      </defs>
      <rect width="97" height="139" fill="url(#photoB)"/>
    </svg>

    <div class="attorney-names">
      <span class="attorney-name attorney-name--first">KEITH A. GARNETT</span>
      <span class="attorney-name attorney-name--second">OWEN LYLE</span>
    </div>
  </div>
</body>
</html>
```